Bramble Bunnies Business Cards

I need a business card for my new Company called Bramble Bunnies. We create handmade baby moccasins, headbands, t-shirts and more. I want some that will appeal to parents, and to go with the colors of my logo that I have attached. feel free to be creative. I would like my logo placed somewhere on the card.

Industry/Entity Type

Retail

Contact Information for Business Card

Bramble Bunnies
20418 Wexley C #5127
Irvine Ca 92687
Rosalind Hatchett Ceo
Info@Bramble-Bunnies.com
www.Bramble-Bunnies.com
Phone 9495817302

Requirements
Nice to have
• Logo included

```html
<!DOCTYPE html>
<html lang="en">
<head>
<meta charset="utf-8">
<title>Bramble Bunnies – Business Card</title>
<link rel="stylesheet" href="https://fonts.googleapis.com/css2?family=Open+Sans:wght@400;600;700&display=swap">
<style>
  :root {
    --page-bg: #ecebea;
    --card-bg: #ffffff;
    --card-shade: #f1f1f1;
    --ink: #1f1f1f;
    --muted: #5c5c5c;
    --accent: #f0955f;
    --accent-soft: #f6c3a4;
    --rule: #9a9a9a;
    --ghost: rgba(0, 0, 0, 0.05);
  }
  html, body {
    margin: 0;
    padding: 0;
    width: 1200px;
    height: 1022px;
    overflow: hidden;
    background: var(--page-bg);
    font-family: "Open Sans", Arial, sans-serif;
  }
  .canvas {
    width: 1200px;
    height: 1022px;
    display: flex;
    align-items: center;
    justify-content: center;
  }
  .card {
    position: relative;
    width: 1050px;
    height: 600px;
    border-radius: 22px;
    background: linear-gradient(160deg, var(--card-bg) 0%, var(--card-shade) 100%);
    box-shadow: 0 10px 30px rgba(0, 0, 0, 0.12);
    overflow: hidden;
    box-sizing: border-box;
    padding: 56px 64px;
  }
  .card__ghost-mark {
    position: absolute;
    left: 90px;
    top: 150px;
    width: 300px;
    height: 300px;
    border-radius: 36px;
    background: var(--ghost);
  }
  .brand {
    position: relative;
    display: flex;
    align-items: center;
    gap: 24px;
  }
  .brand__square {
    width: 64px;
    height: 64px;
    border-radius: 8px;
    background: var(--accent);
    flex: none;
  }
  .brand__name {
    margin: 0;
    font-size: 68px;
    font-weight: 400;
    color: var(--ink);
    letter-spacing: 0.5px;
    line-height: 1;
  }
  .person {
    position: relative;
    margin: 26px 0 0 88px;
    display: flex;
    align-items: baseline;
    gap: 16px;
  }
  .person__name {
    margin: 0;
    font-size: 42px;
    font-weight: 700;
    color: var(--ink);
  }
  .person__title {
    font-size: 24px;
    color: var(--accent);
  }
  .address {
    position: relative;
    margin: 14px 0 0 88px;
    font-size: 24px;
    line-height: 1.35;
    color: var(--muted);
    font-style: normal;
  }
  .rule {
    position: relative;
    height: 0;
    border: 0;
    border-top: 2px solid var(--rule);
    margin: 22px 0 0 0;
  }
  .contacts {
    position: absolute;
    left: 64px;
    right: 64px;
    bottom: 48px;
  }
  .contacts__list {
    list-style: none;
    margin: 18px 0 0 0;
    padding: 0;
  }
  .contacts__item {
    display: flex;
    align-items: center;
    gap: 18px;
    font-size: 24px;
    line-height: 1.45;
    color: var(--muted);
  }
  .contacts__icon {
    width: 22px;
    height: 22px;
    flex: none;
    stroke: var(--accent);
    fill: none;
    stroke-width: 2;
  }
</style>
</head>
<body>
<main class="canvas">
  <article class="card">
    <div class="card__ghost-mark" aria-hidden="true"></div>

    <header class="brand">
      <span class="brand__square" aria-hidden="true"></span>
      <h1 class="brand__name">Bramble Bunnies</h1>
    </header>

    <div class="person">
      <h2 class="person__name">Rosalind Hatchett</h2>
      <span class="person__title">Ceo</span>
    </div>

    <address class="address">
      Bramble Bunnies 20418 Wexley C<br>
      #5127 Irvine Ca 92687
    </address>

    <hr class="rule">

    <section class="contacts">
      <hr class="rule">
      <ul class="contacts__list">
        <li class="contacts__item">
          <svg class="contacts__icon" viewBox="0 0 24 24" aria-hidden="true">
            <path d="M5 3h4l2 5-3 2a12 12 0 0 0 6 6l2-3 5 2v4a2 2 0 0 1-2 2A18 18 0 0 1 3 5a2 2 0 0 1 2-2z"/>
          </svg>
          <span>9495817302</span>
        </li>
        <li class="contacts__item">
          <svg class="contacts__icon" viewBox="0 0 24 24" aria-hidden="true">
            <circle cx="12" cy="12" r="9"/>
            <path d="M3 12h18M12 3c3 3 3 15 0 18M12 3c-3 3-3 15 0 18"/>
          </svg>
          <span>www.Bramble-Bunnies.com</span>
        </li>
        <li class="contacts__item">
          <svg class="contacts__icon" viewBox="0 0 24 24" aria-hidden="true">
            <rect x="3" y="5" width="18" height="14" rx="2"/>
            <path d="M3 7l9 6 9-6"/>
          </svg>
          <span>Info@Bramble-Bunnies.com</span>
        </li>
      </ul>
    </section>
  </article>
</main>
</body>
</html>
```